Rock, Paper Scissors Championship Flyer

We need a dynamic, bold and exciting flyer to promote the following event at our sports center. The event will be primarily focused for adults, but children are welcome to join

Rock, Paper, Scissors Championship - $$$ prizes
Date: June 9th, 2018
Time: 11am-4pm
Fee: $2 to enter, free for spectators
Heats to determine the overall ‘Rock, Paper, Scissors’ champion!
- Cash prizes on offer
- Live music.
- Food and beverage available for purchase

Belvorrow Sports Center, Harwick Glen
908-555-3162
www.belvorrowgrounds.example

Must include our logo (does not have to be huge) and County seal (both attached)

Colors

Designer to choose colors to be used in the design.

Requirements
Must have
• Should be fun and colorful
• The following info and attached logos:
• Rock, Paper, Scissors Championship - $$$ prizes
• Date: June 9th, 2018
• Time: 11am-4pm
• Fee: $2 to enter, free for spectators
• Heats to determine the overall ‘Rock, Paper, Scissors’ champion!
• - Cash prizes on offer
• - Live music.
• - Food and beverage available for purchase
• Belvorrow Sports Center, Harwick Glen
• 908-555-3162
• www.belvorrowgrounds.example
Nice to have
• There are a few inspirational photos attached to give an idea of what we are looking for.

```html
<!DOCTYPE html>
<html lang="en">
<head>
<meta charset="utf-8">
<title>Rock, Paper, Scissors Championship</title>
<link href="https://fonts.googleapis.com/css2?family=Fira+Sans:wght@800&family=Roboto:wght@700&family=Roboto+Condensed:wght@700&family=Yellowtail&display=swap" rel="stylesheet">
<style>
  :root {
    --navy: #123f68;
    --ink: #173e6a;
    --bar: #3a3a3a;
    --white: #ffffff;
    --paper: #f4f5f7;
    --stage: #e6e7e9;
    --photo-top: #2a2420;
    --photo-mid: #3e342d;
    --photo-low: #4a3526;
    --seal: #c9b57a;
  }
  html, body { margin: 0; padding: 0; }
  body {
    width: 988px; height: 1200px; overflow: hidden;
    background: var(--stage);
  }
  .flyer {
    position: absolute; left: 71px; top: 0;
    width: 846px; height: 1200px; overflow: hidden;
    background: linear-gradient(90deg, var(--white) 0%, var(--paper) 100%);
    font-family: "Roboto", Arial, sans-serif;
    color: var(--ink);
  }
  .header { position: absolute; left: 0; top: 0; width: 846px; height: 460px; }
  .details { position: absolute; left: 56px; top: 0; }
  .detail {
    position: absolute; left: 0; width: 330px;
    border-left: 3px solid var(--bar);
    padding-left: 16px;
    font-size: 26px; line-height: 31px; font-weight: 700;
    white-space: nowrap;
  }
  .hands {
    position: absolute; left: 470px; top: 488px; width: 150px; height: 345px;
    background: radial-gradient(ellipse at center, #eef1f6 0%, rgba(238,241,246,0) 70%);
  }
  .center-mark {
    position: absolute; left: 622px; top: 520px; width: 186px;
    text-align: center; font-family: "Roboto Condensed", "Roboto", Arial, sans-serif;
    font-size: 26px; line-height: 30px; font-weight: 700;
    color: var(--ink); white-space: nowrap;
  }
  .center-mark .dot {
    display: block; width: 36px; height: 36px; border-radius: 50%;
    background: var(--navy); margin: 0 auto 10px;
  }
  .seal {
    position: absolute; left: 639px; top: 680px; width: 148px; height: 148px;
    border-radius: 50%; background: var(--seal);
  }
  .tagline {
    position: absolute; left: 0; top: 880px; width: 846px; text-align: center;
    font-family: "Yellowtail", "Brush Script MT", cursive; font-size: 36px; line-height: 40px;
    color: var(--ink);
  }
  .footer { position: absolute; left: 0; top: 970px; width: 846px; height: 230px; }
  .contact {
    position: absolute; left: 0; top: 1075px; width: 846px; text-align: center;
    color: var(--white); font-size: 25px; line-height: 34px; font-weight: 700;
  }
</style>
</head>
<body>
<div class="flyer">
  <svg class="header" viewBox="0 0 846 460" xmlns="http://www.w3.org/2000/svg">
    <defs>
      <linearGradient id="night" x1="0" y1="0" x2="0" y2="1">
        <stop offset="0" stop-color="#2a2420"/>
        <stop offset="0.7" stop-color="#3e342d"/>
        <stop offset="1" stop-color="#4a3526"/>
      </linearGradient>
    </defs>
    <path role="img" aria-label="Blurred evening crowd under string lights at an outdoor venue" d="M0,0 L846,0 L846,342 L790,346 L740,350 L690,348 L640,352 L600,356 L560,364 L530,372 L500,390 L480,400 L460,418 L440,428 L425,448 L415,430 L400,420 L380,395 L360,372 L330,358 L290,362 L240,350 L190,356 L140,350 L90,352 L40,345 L0,340 Z" fill="url(#night)"/>
    <path id="arc1" d="M40,198 Q423,40 806,198" fill="none"/>
    <path id="arc2" d="M70,300 Q423,140 776,300" fill="none"/>
    <g font-family="Fira Sans, Arial, sans-serif" font-weight="800" fill="#ffffff">
      <text font-size="54"><textPath href="#arc1" startOffset="50%" text-anchor="middle">ROCK, PAPER, SCISSORS</textPath></text>
      <text font-size="96"><textPath href="#arc2" startOffset="50%" text-anchor="middle">CHAMPIONSHIP</textPath></text>
      <text x="423" y="300" font-size="52" text-anchor="middle">$$$ PRIZES</text>
    </g>
  </svg>

  <div class="details">
    <div class="detail" style="top:488px">June 9th, 2018<br>11am-4pm</div>
    <div class="detail" style="top:580px">$2 TO ENTER<br>Free For Spectators</div>
    <div class="detail" style="top:672px">Cash Prizes on Offer<br>Live Music</div>
    <div class="detail" style="top:764px">Food and beverage<br>available for purchase</div>
  </div>

  <div class="hands" role="img" aria-label="Outlined cartoon gloved hands showing rock, scissors and paper"></div>

  <div class="center-mark"><span class="dot"></span>BELVORROW<br>SPORTS CENTER</div>
  <div class="seal" role="img" aria-label="County seal badge"></div>

  <div class="tagline">Heats to determine the overall<br>Rock, Paper, Scissors’ champion!</div>

  <svg class="footer" viewBox="0 0 846 230" xmlns="http://www.w3.org/2000/svg">
    <path d="M0,20 L40,14 L90,10 L140,18 L190,8 L240,14 L290,22 L330,40 L370,60 L400,80 L425,103 L450,80 L490,55 L530,38 L570,22 L610,14 L660,6 L710,12 L760,8 L810,4 L846,0 L846,230 L0,230 Z" fill="#123f68"/>
  </svg>
  <div class="contact">Belvorrow Sports Center, Harwick Glen<br>908-555-3162 | www.belvorrowgrounds.example</div>
</div>
</body>
</html>
```